Online Marketing Website

Create a website design for an online marketing company.

It should use modern designs:

Power of space,
Graphics supported content - less words more meaning
Grid and flow layout for listing type content
Provision for responsive and interactive CSS

http://www.bluelanternworks.com.au/ is a very quick mock up, however this should only be used as an example and is not a indication of desired design. Examples that differ from this will be considered.
Updates

To all the developers who have submitted a design, There are a lot a great designs there. I am going to wait a little while longer before providing any feedback as I do not like wasting your time, and experience has shown good designs come late.

At this stage no news is not bad news... It is just that.

Thanks heaps for your work, will contact the leaders soon.

Target Market(s)

Small to Medium Business operating in the B2B or professional B2C space

Industry/Entity Type

Marketing

Requirements
Must have
• It should use a modern Panel design for the front page that will give a high level overview of the products with in-depth content pages for each service.

Nice to have
• Rotating banner at the top of the pages, no higher than 300px

Appropriate use of power colours such as red and Orange.
Should not have
• No Sidebars except on Post pages

```html
<!DOCTYPE html>
<html lang="en">
<head>
<meta charset="utf-8">
<title>Blue Lantern Works</title>
<link href="https://fonts.googleapis.com/css2?family=Mulish:wght@400;700;800&family=Source+Sans+3:wght@400;500&display=swap" rel="stylesheet">
<style>
  :root {
    --ink-black: #000000;
    --white: #ffffff;
    --banner-dark: #1b1b1b;
    --footer-upper: #222222;
    --footer-lower: #1a1a1a;
    --rule-grey: #8a8a8a;
    --brand-red: #d93034;
    --heading-red: #e0242c;
    --body-grey: #7d8b96;
    --menu-grey: #6f7a82;
    --frame-grey: #d7d7d7;
    --panel-orange: #ff5a12;
    --panel-cream: #e3e0ae;
    --panel-cyan: #12b6de;
    --panel-green: #8cc933;
    --panel-red: #e61f2a;
  }
  * { margin: 0; padding: 0; box-sizing: border-box; }
  html, body { width: 1200px; height: 838px; overflow: hidden; background: var(--white); }
  body { position: relative; font-family: "Mulish", sans-serif; }

  .top-strip { position: absolute; left: 0; top: 0; width: 1200px; height: 22px; background: var(--ink-black); }

  .site-header { position: absolute; left: 0; top: 22px; width: 1200px; height: 76px; background: var(--white); }
  .brand { position: absolute; left: 248px; top: 22px; display: flex; align-items: center; gap: 8px; }
  .brand-mark { width: 20px; height: 20px; background: var(--brand-red); }
  .brand-name { font-weight: 800; font-size: 11px; color: var(--brand-red); letter-spacing: 0.1px; text-transform: uppercase; }
  .main-nav { position: absolute; left: 883px; top: 34px; font-family: "Source Sans 3", sans-serif; font-size: 8px; color: var(--menu-grey); letter-spacing: 0.3px; }

  .hero-banner { position: absolute; left: 0; top: 98px; width: 1200px; height: 219px; background: var(--banner-dark); }
  .hero-banner::before { content: ""; position: absolute; left: 0; top: 0; width: 211px; height: 3px; background: var(--rule-grey); }
  .hero-panels { position: absolute; left: 211px; top: 0; width: 777px; height: 219px; display: flex; }
  .hero-panel { flex: 1; height: 100%; }
  .hero-panel.orange { background: linear-gradient(160deg, #ff7a1a, var(--panel-orange) 55%, #ff4a0c); }
  .hero-panel.cream  { background: linear-gradient(160deg, #ecebc4, var(--panel-cream) 55%, #d9d69c); }
  .hero-panel.cyan   { background: linear-gradient(160deg, #0fd6ee, var(--panel-cyan) 55%, #1aa0d8); }
  .hero-panel.green  { background: linear-gradient(160deg, #b4e050, var(--panel-green) 55%, #6cb82a); }
  .hero-panel.red    { background: linear-gradient(160deg, #f0343c, var(--panel-red) 55%, #dc1620); }

  .service-grid { position: absolute; left: 242px; top: 330px; width: 740px; display: flex; }
  .service-item { width: 184.5px; }
  .service-icon { display: block; width: 127px; height: 111px; }
  .service-text { margin-top: 21px; width: 160px; font-size: 8.6px; line-height: 15px; color: var(--body-grey); }

  .feature-photo { position: absolute; left: 242px; top: 524px; width: 269px; height: 178px; border: 3px solid var(--frame-grey);
    background: linear-gradient(180deg, #e9ebee 0%, #b9c6d2 45%, #3f78b0 80%, #1f3f6a 100%); }

  .feature-copy { position: absolute; left: 610px; top: 527px; width: 356px; }
  .feature-title { font-family: "Source Sans 3", sans-serif; font-weight: 400; font-size: 18px; color: var(--heading-red); letter-spacing: -0.4px; line-height: 20px; }
  .feature-text { margin-top: 33px; font-size: 8.6px; line-height: 15.2px; color: var(--body-grey); }

  .footer-widgets { position: absolute; left: 0; top: 702px; width: 1200px; height: 64px; background: var(--footer-upper); }
  .site-footer { position: absolute; left: 0; top: 766px; width: 1200px; height: 60px; background: var(--footer-lower); }
  .footer-text { position: absolute; left: 242px; top: 33px; font-size: 8px; line-height: 16px; color: var(--white); }
  .bottom-strip { position: absolute; left: 0; top: 826px; width: 1200px; height: 12px; background: var(--ink-black); }
</style>
</head>
<body>
  <div class="top-strip"></div>

  <header class="site-header">
    <div class="brand">
      <span class="brand-mark"></span>
      <span class="brand-name">Blue Lantern Works</span>
    </div>
    <nav class="main-nav">NO MENU ASSIGNED!</nav>
  </header>

  <section class="hero-banner">
    <div class="hero-panels" role="img" aria-label="Rotating banner of five textured colour panels: orange, cream, cyan, green and red">
      <div class="hero-panel orange"></div>
      <div class="hero-panel cream"></div>
      <div class="hero-panel cyan"></div>
      <div class="hero-panel green"></div>
      <div class="hero-panel red"></div>
    </div>
  </section>

  <section class="service-grid">
    <article class="service-item">
      <svg class="service-icon" viewBox="0 0 127 111" aria-hidden="true">
        <g fill="#d93034">
          <ellipse cx="96" cy="31" rx="15" ry="18"/>
          <path d="M78 52 Q96 62 114 52 L124 70 Q127 76 127 84 L127 111 L100 111 L100 92 Q96 82 84 76 Z"/>
          <ellipse cx="39" cy="24" rx="21" ry="24"/>
          <path d="M14 50 Q39 66 64 50 L78 70 Q88 76 88 84 L88 111 L0 111 L0 84 Q0 74 8 68 Z"/>
        </g>
      </svg>
      <p class="service-text">Proin gravida nibh vel velit auctor aliquet. Aenean sollicitudin, lorem quis bibendum auctor, nisi elit consequat ipsum, nec sagittis.</p>
    </article>
    <article class="service-item">
      <svg class="service-icon" viewBox="0 0 127 111" aria-hidden="true">
        <g fill="#d93034">
          <ellipse cx="96" cy="31" rx="15" ry="18"/>
          <path d="M78 52 Q96 62 114 52 L124 70 Q127 76 127 84 L127 111 L100 111 L100 92 Q96 82 84 76 Z"/>
          <ellipse cx="39" cy="24" rx="21" ry="24"/>
          <path d="M14 50 Q39 66 64 50 L78 70 Q88 76 88 84 L88 111 L0 111 L0 84 Q0 74 8 68 Z"/>
        </g>
      </svg>
      <p class="service-text">Proin gravida nibh vel velit auctor aliquet. Aenean sollicitudin, lorem quis bibendum auctor, nisi elit consequat ipsum, nec sagittis.</p>
    </article>
    <article class="service-item">
      <svg class="service-icon" viewBox="0 0 127 111" aria-hidden="true">
        <g fill="#d93034">
          <ellipse cx="96" cy="31" rx="15" ry="18"/>
          <path d="M78 52 Q96 62 114 52 L124 70 Q127 76 127 84 L127 111 L100 111 L100 92 Q96 82 84 76 Z"/>
          <ellipse cx="39" cy="24" rx="21" ry="24"/>
          <path d="M14 50 Q39 66 64 50 L78 70 Q88 76 88 84 L88 111 L0 111 L0 84 Q0 74 8 68 Z"/>
        </g>
      </svg>
      <p class="service-text">Proin gravida nibh vel velit auctor aliquet. Aenean sollicitudin, lorem quis bibendum auctor, nisi elit.</p>
    </article>
    <article class="service-item">
      <svg class="service-icon" viewBox="0 0 127 111" aria-hidden="true">
        <g fill="#d93034">
          <ellipse cx="96" cy="31" rx="15" ry="18"/>
          <path d="M78 52 Q96 62 114 52 L124 70 Q127 76 127 84 L127 111 L100 111 L100 92 Q96 82 84 76 Z"/>
          <ellipse cx="39" cy="24" rx="21" ry="24"/>
          <path d="M14 50 Q39 66 64 50 L78 70 Q88 76 88 84 L88 111 L0 111 L0 84 Q0 74 8 68 Z"/>
        </g>
      </svg>
      <p class="service-text">Proin gravida nibh vel velit auctor aliquet. Aenean sollicitudin, lorem quis bibendum auctor, nisi elit consequat ipsum, nec sagittis sem.</p>
    </article>
  </section>

  <div class="feature-photo" role="img" aria-label="Photo of office workers holding question-mark cards in front of themselves"></div>

  <section class="feature-copy">
    <h2 class="feature-title">IDENTIFY YOUR CUSTOMERS</h2>
    <p class="feature-text">Proin gravida nibh vel velit auctor aliquet. Aenean sollicitudin, lorem quis bibendum auctor, nisi elit consequat ipsum, nec sagittis sem nibh id elit. Duis sed odio sit amet nibh vulputate cursus a sit amet mauris. Morbi accumsan ipsum velit. Nam nec tellus a odio tincidunt auctor a ornare odio.</p>
  </section>

  <div class="footer-widgets"></div>
  <footer class="site-footer">
    <p class="footer-text">© Copyright 2014<br>Blue Lantern Works</p>
  </footer>
  <div class="bottom-strip"></div>
</body>
</html>
```